Banner Design for Physiotherapy Business

I need a banner designed for a physiotherapy business. The word ‘Physiotherapy’ should be prominent at the top. I’ve attached a document outlining what text and a suggestion of a picture I’d like included. The photo I have suggested in the document won’t upload to artvolley though as the dimensions are too large. I am open to other photos being used though. I would like to see designs that use the colour orange (as seen in the example) or green preferrably. The dimensions need to be 841mm x 2055mm and provided in PDF, JPG, and PNG format and 300dpi in CMYK colour mode.

```html
<!DOCTYPE html>
<html lang="en">
<head>
<meta charset="utf-8">
<title>Physiotherapy Banner</title>
<link rel="stylesheet" href="https://fonts.googleapis.com/css2?family=Lato:wght@400;700;900&family=Raleway:wght@600&display=swap">
<style>
  :root {
    --orange: #e8731c;
    --orange-deep: #e06612;
    --yellow: #fdd835;
    --yellow-soft: #fde98a;
    --amber: #f9a825;
    --white: #ffffff;
    --photo-light: #e9e6e2;
    --photo-mid: #b9b3ad;
    --photo-dark: #8c8580;
  }
  html, body {
    margin: 0;
    padding: 0;
    width: 1200px;
    height: 2821px;
    overflow: hidden;
    background: var(--white);
  }
  .banner {
    position: relative;
    width: 1200px;
    height: 2821px;
    background: var(--white);
    font-family: "Lato", Arial, sans-serif;
    overflow: hidden;
  }
  .top-band {
    position: absolute;
    left: 0; top: 0;
    width: 1200px; height: 58px;
    background: var(--orange);
  }
  .top-band-light {
    position: absolute;
    left: 0; top: 58px;
    width: 1200px; height: 44px;
    background: var(--yellow-soft);
  }
  .top-band-accent {
    position: absolute;
    left: 0; top: 102px;
    width: 1200px; height: 26px;
    background: var(--yellow);
  }
  .title {
    position: absolute;
    left: 0; top: 128px;
    width: 1200px;
    margin: 0;
    text-align: center;
    font-family: "Raleway", "Lato", sans-serif;
    font-weight: 600;
    font-size: 138px;
    line-height: 160px;
    letter-spacing: 1px;
    color: var(--orange);
  }
  .hero-photo {
    position: absolute;
    left: 0; top: 291px;
    width: 1200px; height: 1060px;
    background: linear-gradient(160deg, var(--photo-light) 0%, #d8d3ce 45%, var(--photo-mid) 75%, var(--photo-dark) 100%);
  }
  .hero-swoosh {
    position: absolute;
    left: 0; top: 1000px;
    width: 1200px; height: 380px;
  }
  .services {
    position: absolute;
    left: 0; top: 1425px;
    width: 1200px;
  }
  .services-heading {
    margin: 0 0 0 199px;
    font-weight: 400;
    font-size: 46px;
    line-height: 70px;
    color: var(--orange-deep);
    letter-spacing: 0.5px;
  }
  .services-list {
    list-style: none;
    margin: 6px 0 0 0;
    padding: 0;
  }
  .service {
    position: relative;
    padding-left: 135px;
    font-weight: 700;
    font-size: 40px;
    line-height: 70.5px;
    color: var(--orange);
  }
  .service::before {
    content: "";
    position: absolute;
    left: 92px; top: 31px;
    width: 11px; height: 11px;
    border-radius: 50%;
    background: var(--orange);
  }
  .service-note {
    display: block;
    margin-top: -14px;
    margin-bottom: 4px;
    font-size: 32px;
    line-height: 44px;
    font-weight: 700;
  }
  .footer-rule {
    position: absolute;
    left: 0; top: 2548px;
    width: 1200px; height: 3px;
    background: var(--amber);
  }
  .member-mark {
    position: absolute;
    left: 48px; top: 2585px;
    display: flex;
    align-items: center;
    gap: 22px;
  }
  .member-dot {
    width: 130px; height: 130px;
    border-radius: 50%;
    background: var(--orange);
  }
  .member-name {
    font-weight: 400;
    font-size: 34px;
    line-height: 40px;
    color: var(--orange);
  }
  .appointment {
    position: absolute;
    left: 632px; top: 2555px;
    width: 520px;
    color: var(--orange);
  }
  .appointment-heading {
    margin: 0;
    font-weight: 700;
    font-size: 37px;
    line-height: 52px;
    padding-bottom: 4px;
    border-bottom: 3px solid var(--orange);
  }
  .appointment-address {
    margin: 8px 0 0 0;
    font-style: normal;
    font-weight: 700;
    font-size: 31px;
    line-height: 40px;
  }
  .appointment-phone {
    display: flex;
    align-items: center;
    gap: 18px;
    margin-top: 6px;
    font-weight: 700;
    font-size: 45px;
    line-height: 56px;
  }
  .phone-icon {
    width: 30px; height: 36px;
  }
  .bottom-band-light {
    position: absolute;
    left: 0; top: 2755px;
    width: 1200px; height: 32px;
    background: var(--yellow);
  }
  .bottom-band {
    position: absolute;
    left: 0; top: 2787px;
    width: 1200px; height: 34px;
    background: var(--orange);
  }
</style>
</head>
<body>
<div class="banner">
  <div class="top-band"></div>
  <div class="top-band-light"></div>
  <div class="top-band-accent"></div>

  <h1 class="title">PHYSIOTHERAPY</h1>

  <div class="hero-photo" role="img" aria-label="Photo of a physiotherapist stretching the leg and shoulder of a patient lying on a treatment table in a bright clinic room"></div>

  <svg class="hero-swoosh" viewBox="0 0 1200 380" preserveAspectRatio="none" aria-hidden="true">
    <path d="M0 250 C 300 170, 700 110, 1200 40 L1200 380 L0 380 Z" fill="#f9a825"/>
    <path d="M0 275 C 320 205, 720 150, 1200 95 L1200 380 L0 380 Z" fill="#fdd835"/>
    <path d="M0 300 C 340 240, 740 190, 1200 150 L1200 380 L0 380 Z" fill="#e8731c"/>
    <path d="M0 325 C 360 275, 760 230, 1200 205 L1200 380 L0 380 Z" fill="#fde98a"/>
    <path d="M0 345 C 380 300, 780 265, 1200 250 L1200 380 L0 380 Z" fill="#ffffff"/>
  </svg>

  <section class="services">
    <h2 class="services-heading">WHAT WE TREAT / SERVICES</h2>
    <ul class="services-list">
      <li class="service">Arthritis</li>
      <li class="service">Back pain / Neck pain</li>
      <li class="service">Sciatic pain</li>
      <li class="service">Sports injuries</li>
      <li class="service">Repetitive strain injuries</li>
      <li class="service">Post surgical management
        <span class="service-note">(hip and knee arthroscopes, joint replacement surgery)</span></li>
      <li class="service">Shoulder pain and dysfunction</li>
      <li class="service">Tennis elbow</li>
      <li class="service">Postural pain</li>
      <li class="service">Workplace injuries</li>
      <li class="service">Motor vehicle accidents</li>
      <li class="service">Women’s health issues</li>
      <li class="service">Clinical exercise</li>
      <li class="service">Pre-employment functional assessments</li>
    </ul>
  </section>

  <div class="footer-rule"></div>

  <div class="member-mark">
    <div class="member-dot"></div>
    <div class="member-name">COASTAL<br>PHYSIO GUILD<br>Member</div>
  </div>

  <div class="appointment">
    <h3 class="appointment-heading">MAKE AN APPOINTMENT</h3>
    <address class="appointment-address">Maple Lane Family Practice<br>18-20 Elmwood Rd Fernvale VIC 3199</address>
    <div class="appointment-phone">
      <svg class="phone-icon" viewBox="0 0 30 36" aria-hidden="true">
        <path d="M8 2 L12 10 L9 13 C10 18 13 22 17 25 L20 22 L28 26 L25 33 C12 32 3 20 2 6 Z" fill="none" stroke="#e8731c" stroke-width="3" stroke-linejoin="round"/>
      </svg>
      <span>(03) 9555 0142</span>
    </div>
  </div>

  <div class="bottom-band-light"></div>
  <div class="bottom-band"></div>
</div>
</body>
</html>
```